Brightwell Systems - Company Overview Brochure

We would like a single page A4 Brochure to give to new potential customers to provide a quick overview of our company. This will be used in presales meetings.

We have included the content we would like on the brochure under "Brightwell Systems Marketing Brochure.docx".

We have included two other designs "timebundleterms v4.pdf and Brightwell Public Cloud Plans.pdf" which shows similar marketing brochures we have. We would like these designs to have the same Brightwell Blue and "Specialised Technology Consultancy firm" theme.

Target Market(s)

Technology Sector

Industry/Entity Type

Information Technology

Colors
0054AA
0677BA
7BADD7
CADEEF
E8F1F8

Requirements
Must have
• "Innovative Tech Company Theme".

```html
<!DOCTYPE html>
<html lang="en">
<head>
<meta charset="utf-8">
<title>Brightwell Systems – Company Overview</title>
<link rel="stylesheet" href="https://fonts.googleapis.com/css2?family=Montserrat:wght@500;600;700&family=Open+Sans:wght@400;600&family=Barlow+Semi+Condensed:wght@600&family=Kaushan+Script&display=swap">
<style>
  :root {
    --navy: #232d80;
    --navy-deep: #141d63;
    --navy-ink: #1a2466;
    --brand-blue: #0054AA;
    --accent-blue: #0677BA;
    --sky: #7BADD7;
    --mist: #CADEEF;
    --ice: #E8F1F8;
    --white: #ffffff;
    --cyan-glow: #4fd2f0;
  }
  * { box-sizing: border-box; margin: 0; padding: 0; }
  html, body { width: 960px; height: 1200px; overflow: hidden; background: var(--white); }
  .brochure { position: relative; width: 960px; height: 1200px; background: var(--white); font-family: "Open Sans", sans-serif; }

  /* Header */
  .hero { position: absolute; left: 0; top: 0; width: 960px; height: 500px; overflow: hidden;
    background: linear-gradient(160deg, #2a3690 0%, var(--navy) 55%, #1c2672 100%); }
  .hero-circuit { position: absolute; left: 480px; top: 0; width: 480px; height: 360px;
    background: radial-gradient(ellipse at 75% 35%, rgba(79,210,240,.28), rgba(79,210,240,0) 65%); }
  .hero-corner { position: absolute; left: 0; top: 0; }
  .brand { position: absolute; left: 26px; top: 44px; display: flex; align-items: center; gap: 12px; }
  .brand-mark { width: 30px; height: 30px; background: var(--navy-ink); }
  .brand-name { font-family: "Montserrat", sans-serif; font-weight: 700; font-size: 27px; color: var(--navy-ink); letter-spacing: 0.5px; }
  .tagline-kicker { position: absolute; left: 552px; top: 46px; font-family: "Montserrat", sans-serif; font-weight: 600;
    font-size: 19px; color: var(--white); }
  .hero-title { position: absolute; left: 0; width: 960px; top: 146px; text-align: center; font-family: "Montserrat", sans-serif;
    font-weight: 600; font-size: 35px; color: var(--white); }
  .hero-sub { position: absolute; left: 0; width: 960px; top: 194px; text-align: center; font-family: "Montserrat", sans-serif;
    font-weight: 500; font-size: 17px; color: var(--white); }
  .hero-photo { position: absolute; left: 0; top: 241px; width: 960px; height: 259px;
    background: linear-gradient(90deg, #2b3466 0%, #5a6690 30%, #7a7c8c 45%, #3b4a86 65%, #283a86 85%, #3a78b8 100%); }
  .hero-curve { position: absolute; left: 0; top: 440px; }

  /* Section headings */
  .section-head { position: absolute; left: 0; width: 960px; display: flex; align-items: center; justify-content: center; gap: 10px; }
  .section-head::before, .section-head::after { content: ""; height: 2px; background: var(--navy-ink); }
  .section-head h2 { font-family: "Montserrat", sans-serif; font-weight: 600; font-size: 32px; color: var(--navy-ink); }
  .commitment-head { top: 520px; }
  .commitment-head::before, .commitment-head::after { width: 218px; }
  .commitment-lead { position: absolute; left: 0; width: 960px; top: 575px; text-align: center; font-family: "Montserrat", sans-serif;
    font-weight: 600; font-size: 20px; color: var(--accent-blue); }

  .pillars { position: absolute; left: 170px; top: 620px; width: 620px; display: flex; justify-content: space-between; }
  .pillar { width: 200px; display: flex; flex-direction: column; align-items: center; }
  .pillar svg { height: 118px; }
  .pillar-label { margin-top: 20px; font-family: "Barlow Semi Condensed", sans-serif; font-weight: 600; font-size: 23px; color: var(--navy-ink); }

  .policy-head { top: 788px; gap: 28px; }
  .policy-head::before, .policy-head::after { width: 270px; }

  /* Policy */
  .policy { position: absolute; left: 0; top: 839px; width: 960px; height: 361px;
    background: linear-gradient(180deg, #2b3588 0%, #27328a 50%, #232c7c 100%); }
  .policy-panel { position: absolute; left: 0; top: 0; }
  .policy-item { position: absolute; top: 22px; text-align: center; color: var(--white); }
  .policy-item h3 { font-family: "Montserrat", sans-serif; font-style: italic; font-weight: 700; font-size: 33px; padding-bottom: 6px;
    border-bottom: 2px solid var(--white); display: inline-block; }
  .policy-item p { margin-top: 16px; font-size: 17px; line-height: 22px; }
  .policy-fair { left: 90px; width: 240px; }
  .policy-fair h3 { width: 180px; }
  .policy-cost { left: 590px; width: 330px; top: 16px; }
  .policy-cost h3 { padding: 0 6px 6px; }
  .policy-centre { position: absolute; left: 380px; top: 120px; width: 200px; text-align: center;
    font-family: "Open Sans", sans-serif; font-weight: 600; font-size: 26px; color: var(--white); }

  .motto { position: absolute; left: 0; width: 960px; top: 195px; text-align: center; font-family: "Kaushan Script", cursive;
    font-size: 66px; color: var(--white); }
  .motto-swoosh { position: absolute; left: 270px; top: 275px; }
  .terms { position: absolute; left: 0; width: 960px; top: 316px; text-align: center; font-family: "Montserrat", sans-serif;
    font-weight: 500; font-size: 14px; line-height: 21px; color: var(--white); }
  .terms a { color: var(--sky); text-decoration: none; }
</style>
</head>
<body>
<main class="brochure">

  <header class="hero">
    <div class="hero-circuit" role="img" aria-label="Glowing cyan circuit-board traces"></div>
    <svg class="hero-corner" width="960" height="130" viewBox="0 0 960 130">
      <polygon points="0,0 524,0 420,130 0,130" fill="#ffffff"/>
    </svg>
    <div class="brand">
      <span class="brand-mark"></span>
      <span class="brand-name">BRIGHTWELL SYSTEMS</span>
    </div>
    <p class="tagline-kicker">SPECIALISED CONSULTING</p>
    <h1 class="hero-title">Technology Consulting Solutions in Perth, WA</h1>
    <p class="hero-sub">which offers customers tailored technical solutions for a range of products.</p>
    <div class="hero-photo" role="img" aria-label="Montage: engineer at a server rack with a laptop, business handshake, security camera, operator at a monitoring desk, telecom tower and fibre optic cables"></div>
    <svg class="hero-curve" width="960" height="60" viewBox="0 0 960 60">
      <path d="M0,20 Q480,85 960,20 L960,60 L0,60 Z" fill="#ffffff"/>
      <path d="M0,22 Q480,86 960,22" fill="none" stroke="#7BADD7" stroke-width="2"/>
    </svg>
  </header>

  <section>
    <div class="section-head commitment-head"><h2>Our Commitment</h2></div>
    <p class="commitment-lead">We do things right the fist time. Quality solutions ead best practices</p>

    <div class="pillars">
      <div class="pillar">
        <svg viewBox="0 0 120 130" width="110">
          <path d="M60,6 L110,22 L106,70 Q100,108 60,126 Q20,108 14,70 L10,22 Z" fill="#1a2a8a"/>
          <path d="M60,16 L100,29 L96,70 Q91,100 60,115 Z" fill="#CADEEF"/>
          <path d="M60,16 L20,29 L24,70 Q29,100 60,115 Z" fill="#2f5fc0"/>
          <circle cx="60" cy="56" r="11" fill="#141d63"/>
          <path d="M55,62 L65,62 L68,84 L52,84 Z" fill="#141d63"/>
        </svg>
        <span class="pillar-label">Cybersecurity</span>
      </div>
      <div class="pillar">
        <svg viewBox="0 0 170 120" width="170">
          <rect x="5" y="12" width="128" height="28" rx="4" fill="#2b4fa8"/>
          <rect x="5" y="45" width="128" height="28" rx="4" fill="#24438f"/>
          <rect x="5" y="78" width="128" height="28" rx="4" fill="#1d3678"/>
          <g fill="#e6e04a">
            <rect x="14" y="23" width="6" height="5"/><rect x="24" y="23" width="6" height="5"/><rect x="34" y="23" width="6" height="5"/>
            <rect x="14" y="56" width="6" height="5"/><rect x="24" y="56" width="6" height="5"/><rect x="34" y="56" width="6" height="5"/>
            <rect x="14" y="89" width="6" height="5"/><rect x="24" y="89" width="6" height="5"/><rect x="34" y="89" width="6" height="5"/>
          </g>
          <circle cx="132" cy="78" r="34" fill="#1f9a3a"/>
          <path d="M115,78 L128,92 L150,66" fill="none" stroke="#ffffff" stroke-width="9" stroke-linecap="round" stroke-linejoin="round"/>
        </svg>
        <span class="pillar-label">Business Continuity</span>
      </div>
      <div class="pillar">
        <svg viewBox="0 0 170 120" width="170">
          <circle cx="104" cy="52" r="38" fill="none" stroke="#1f3a9a" stroke-width="22" stroke-dasharray="12 8"/>
          <circle cx="104" cy="52" r="30" fill="none" stroke="#1f3a9a" stroke-width="12"/>
          <circle cx="44" cy="70" r="27" fill="none" stroke="#9aa3b8" stroke-width="15" stroke-dasharray="9 6"/>
          <circle cx="44" cy="70" r="21" fill="none" stroke="#aab2c4" stroke-width="9"/>
        </svg>
        <span class="pillar-label">Tailored Solutions</span>
      </div>
    </div>

    <div class="section-head policy-head"><h2>Our Policy</h2></div>
  </section>

  <section class="policy">
    <svg class="policy-panel" width="960" height="170" viewBox="0 0 960 170">
      <defs>
        <linearGradient id="panelFade" x1="0" y1="0" x2="0" y2="1">
          <stop offset="0" stop-color="#141d63"/>
          <stop offset="1" stop-color="#1a2470"/>
        </linearGradient>
      </defs>
      <path d="M27,0 L400,0 Q470,20 480,70 Q490,20 560,0 L940,0 L940,150 L27,150 Z" fill="url(#panelFade)"/>
    </svg>
    <div class="policy-item policy-fair">
      <h3>Be Fair</h3>
      <p>Pricing that<br>balances value and quality</p>
    </div>
    <div class="policy-item policy-cost">
      <h3>Be Cost-Effective</h3>
      <p>High quality services<br>at a fair cost</p>
    </div>
    <p class="policy-centre">Brightwell</p>

    <p class="motto">Do it Once, Do it Right!</p>
    <svg class="motto-swoosh" width="420" height="14" viewBox="0 0 420 14">
      <path d="M0,12 Q210,2 420,0 Q210,6 0,14 Z" fill="#ffffff"/>
    </svg>
    <p class="terms">All goods and services provided by Brightwell are provided in accordance<br>with our Standard Terms and Conditions available at <a href="#">https://www.brightwellsystems.com.au/t&amp;c</a></p>
  </section>

</main>
</body>
</html>
```